Halvex Consulting

Hi,
I have my own network consulting business (just me)
and need to get a logo and business card design together,

Based in New Zealand,

Gareth Pollard
Unified Communications and Network Architect

/design engineer,
and would like this to be the basis for personal branding and company identity

Reason: I will be off site for a couple of days - so you have some more time

Business

• I have the basis for a optional logo - needs color -

```html
<!DOCTYPE html>
<html lang="en">
<head>
<meta charset="utf-8">
<title>Halvex Consulting – Business Card</title>
<link rel="stylesheet" href="https://fonts.googleapis.com/css2?family=Ubuntu:ital,wght@0,300;0,400;0,500;0,700;1,700&display=swap">
<style>
  :root {
    --backdrop: #4a4a4a;
    --card-white: #ffffff;
    --card-black: #0b0b0b;
    --accent-red: #e10b0b;
    --ink-dark: #1c1c1c;
    --ink-grey: #8a8a8a;
    --ink-light: #f2f2f2;
    --mark-blue: #2a8fd4;
  }
  * { box-sizing: border-box; margin: 0; padding: 0; }
  html, body {
    width: 1200px;
    height: 800px;
    overflow: hidden;
    background: var(--backdrop);
    font-family: "Ubuntu", sans-serif;
  }
  .business-card {
    position: absolute;
    left: 100px;
    top: 120px;
    width: 1000px;
    height: 560px;
    background: var(--card-white);
    overflow: hidden;
    box-shadow: 0 12px 30px rgba(0,0,0,0.45);
  }
  .card-bands {
    position: absolute;
    inset: 0;
    width: 1000px;
    height: 560px;
  }
  .brand {
    position: absolute;
    left: 285px;
    top: 82px;
    display: flex;
    align-items: center;
    gap: 28px;
  }
  .brand-text { display: flex; flex-direction: column; }
  .brand-name {
    font-size: 54px;
    font-weight: 700;
    color: var(--ink-dark);
    letter-spacing: -0.5px;
    line-height: 1;
  }
  .brand-tagline {
    margin-top: 6px;
    font-size: 26px;
    font-weight: 300;
    color: var(--ink-grey);
  }
  .brand-dot {
    width: 64px;
    height: 64px;
    border-radius: 50%;
    background: var(--mark-blue);
    flex: none;
  }
  .contact-block {
    position: absolute;
    left: 58px;
    top: 345px;
    color: var(--ink-light);
  }
  .person-name {
    font-size: 33px;
    font-weight: 500;
    color: var(--accent-red);
    line-height: 1.1;
  }
  .person-title {
    font-size: 25px;
    font-weight: 400;
    margin-top: 2px;
  }
  .person-role {
    font-size: 27px;
    font-weight: 700;
    font-style: italic;
    margin-top: 2px;
  }
  .contact-lines {
    margin-top: 26px;
    font-size: 21px;
    font-weight: 300;
    line-height: 1.5;
  }
</style>
</head>
<body>
  <section class="business-card">
    <svg class="card-bands" viewBox="0 0 1000 560" aria-hidden="true">
      <polygon points="0,270 1000,315 1000,560 0,560" fill="var(--accent-red)"/>
      <polygon points="0,288 1000,333 1000,560 0,560" fill="var(--card-black)"/>
    </svg>

    <header class="brand">
      <div class="brand-text">
        <span class="brand-name">Halvex Consulting</span>
        <span class="brand-tagline">network consulting business</span>
      </div>
      <span class="brand-dot"></span>
    </header>

    <div class="contact-block">
      <p class="person-name">Gareth Pollard</p>
      <p class="person-title">Unified Communications and Network Architect</p>
      <p class="person-role">design engineer</p>
      <div class="contact-lines">
        <p>mobile: (+00) 555-0142</p>
        <p>email: hello@halvex.example</p>
      </div>
    </div>
  </section>
</body>
</html>
```